quorvaAgency Business Card Design Project

We need a business card design for quorvaAgency. quorvaAgency is an underwriting agency. Underwriting agencies act on behalf of insurers, to underwrite insurance. We will be operating in specialised classes of insurance initially and looking to expand from there. We would like to see designs that incorporate our logo colours as well as a contrasting stand out colour - also we'd like the logo itself to be embossed on the card.

Industry/Entity Type

Insurance

Requirements
Must have
• Logo on front
Nice to have
• Logo solely featured on back of card
Should not have
• Please do not use comic cans font :)

```html
<!DOCTYPE html>
<html lang="en">
<head>
<meta charset="utf-8">
<title>quorvaAgency Business Card</title>
<link rel="stylesheet" href="https://fonts.googleapis.com/css2?family=Arimo:wght@400;700&display=swap">
<style>
  :root {
    --brand-blue: #1a67b0;
    --brand-blue-dark: #0d4f93;
    --brand-blue-light: #2a82c9;
    --ink: #3a3a3c;
    --ink-soft: #58585a;
    --footer-grey: #414143;
    --card-border: #b9b9bb;
    --page: #ffffff;
  }
  * { margin: 0; padding: 0; box-sizing: border-box; }
  html, body {
    width: 1200px; height: 900px; overflow: hidden;
    background: var(--page);
    font-family: "Arimo", Arial, sans-serif;
  }
  .canvas { position: relative; width: 1200px; height: 900px; }

  .card {
    position: absolute; top: 279px;
    width: 527px; height: 326px;
    border-radius: 12px; overflow: hidden;
  }

  /* Front */
  .card-front {
    left: 40px;
    border: 1.5px solid var(--card-border);
    background: linear-gradient(180deg, #ffffff 0%, #f6f6f7 55%, #ffffff 100%);
  }
  .front-mark {
    position: absolute; left: 112px; top: 36px;
    width: 38px; height: 38px; border-radius: 50%;
    background: var(--brand-blue);
  }
  .front-band {
    position: absolute; top: 106px; height: 20px;
    background: linear-gradient(180deg, var(--brand-blue-light), var(--brand-blue-dark));
  }
  .front-band.left { left: 0; width: 44px; }
  .front-band.right { left: 314px; right: 0; }
  .front-name {
    position: absolute; left: 52px; top: 98px;
    font-size: 31px; font-weight: 700; color: var(--brand-blue);
    letter-spacing: -0.5px; line-height: 1;
  }
  .person {
    position: absolute; right: 290px; top: 176px;
    text-align: right; color: var(--ink);
    font-weight: 700;
  }
  .person-name { font-size: 20px; line-height: 1.25; }
  .person-role { font-size: 17px; line-height: 1.3; color: var(--ink-soft); }
  .divider {
    position: absolute; left: 238px; top: 170px;
    width: 1.5px; height: 76px; background: var(--ink-soft);
  }
  .contacts {
    position: absolute; left: 268px; top: 174px;
    list-style: none; font-size: 12px; color: var(--ink);
  }
  .contacts li { display: flex; align-items: center; height: 17px; }
  .contacts svg { width: 11px; height: 11px; margin-right: 7px; fill: var(--ink); }
  .front-rule {
    position: absolute; left: 30px; top: 281px; width: 420px; height: 1px;
    background: linear-gradient(90deg, transparent, #cfcfd1 20%, #cfcfd1 80%, transparent);
  }
  .front-web {
    position: absolute; left: 125px; top: 284px;
    font-size: 12px; font-weight: 700; letter-spacing: 4.2px; color: var(--ink);
  }

  /* Back */
  .card-back { left: 630px; background: var(--footer-grey); }
  .back-field {
    position: absolute; left: 0; top: 0; right: 0; height: 267px;
    background: radial-gradient(ellipse at 50% 45%, #2a80c6 0%, #1566ad 55%, #0c5598 100%);
    border-bottom: 2px solid #8ab6dc;
    display: flex; flex-direction: column; align-items: center;
  }
  .back-mark {
    margin-top: 62px; width: 80px; height: 80px; border-radius: 50%;
    background: #ffffff;
  }
  .back-name {
    margin-top: 18px;
    font-size: 58px; font-weight: 700; color: #ffffff;
    letter-spacing: -1px; line-height: 1;
  }
  .back-web {
    position: absolute; left: 0; right: 0; top: 285px;
    text-align: center; font-size: 14px; letter-spacing: 2.4px; color: #ffffff;
  }
</style>
</head>
<body>
<main class="canvas">
  <section class="card card-front" aria-label="Business card front">
    <div class="front-mark" aria-hidden="true"></div>
    <div class="front-band left"></div>
    <div class="front-name">quorvaAgency</div>
    <div class="front-band right"></div>

    <div class="person">
      <p class="person-name">Your Name</p>
      <p class="person-role">Current Postion</p>
    </div>
    <div class="divider"></div>
    <ul class="contacts">
      <li><svg viewBox="0 0 12 12"><path d="M2.5 0.8l2 2-1 1.4c.7 1.5 1.8 2.6 3.3 3.3l1.4-1 2 2-1.4 2.1C5 10.4 1.6 7 .4 2.2z"/></svg>012 345 6789</li>
      <li><svg viewBox="0 0 12 12"><path d="M3.5 0h5a1 1 0 0 1 1 1v10a1 1 0 0 1-1 1h-5a1 1 0 0 1-1-1V1a1 1 0 0 1 1-1zm.5 1.5v7h4v-7zM6 9.5a.8.8 0 1 0 0 1.6.8.8 0 0 0 0-1.6z"/></svg>012 345 6789</li>
      <li><svg viewBox="0 0 12 12"><path d="M6 1.5c3.3 0 6 1.8 6 4s-2.7 4-6 4c-.6 0-1.2 0-1.7-.2L1.2 11l.9-2.4C.8 7.9 0 6.8 0 5.5c0-2.2 2.7-4 6-4z"/></svg>yournick@chatline.com</li>
      <li><svg viewBox="0 0 12 12"><path d="M0 2.5h12v7H0zm1 .8L6 6.6l5-3.3z" fill-rule="evenodd"/></svg>yourmail@quorvaagency.com</li>
    </ul>
    <div class="front-rule"></div>
    <p class="front-web">www.yourwebsite.com</p>
  </section>

  <section class="card card-back" aria-label="Business card back">
    <div class="back-field">
      <div class="back-mark" aria-hidden="true"></div>
      <div class="back-name">quorvaAgency</div>
    </div>
    <p class="back-web">www.yourwebsite.com</p>
  </section>
</main>
</body>
</html>
```